CalmHarbor Homepage and Landing Pages

Please see detailed brief.

CalmHarbor is Australia’s newest online therapy and mental health service. We allow patients from across australia to connect with Mental health practitioners from across Australia. Our mission is to remove the friction in gaining support for mental health related issues.

Number of Pages Required

1 page

Font styles to use
Sans Serif

Colors
33a6d7
0293ce
3277b5
0255a3
acd136
9bcb3c

Requirements
Must have
• Please see detailed brief.
Nice to have
• Please see detailed brief
Should not have

```html
<!DOCTYPE html>
<html lang="en">
<head>
<meta charset="utf-8">
<title>CalmHarbor – Practitioner Detail</title>
<link href="https://fonts.googleapis.com/css2?family=Arimo:wght@400;700&display=swap" rel="stylesheet">
<style>
:root{
  --brand:#0aa8f3;
  --brand-dark:#0a5bd6;
  --text:#6e6e6e;
  --text-dark:#555;
  --page-bg:#f2f2f2;
  --footer-bg:#f4f4f4;
  --bar-bg:#e6e6e6;
  --panel-bg:#e8e8e8;
  --white:#fff;
}
*{margin:0;padding:0;box-sizing:border-box}
html,body{width:1200px;height:959px;overflow:hidden}
body{position:relative;background:var(--page-bg);font-family:"Arimo",Arial,sans-serif;color:var(--text)}
.abs{position:absolute}
.site-header{position:absolute;left:0;top:0;width:1200px;height:67px;background:var(--white)}
.brand{display:flex;align-items:center;gap:9px;color:#3a3a3a;font-weight:400}
.brand-dot{border-radius:50%;background:var(--brand)}
.header-brand{left:73px;top:16px;font-size:32px}
.header-brand .brand-dot{width:26px;height:26px}
.main-nav{left:409px;top:27px;display:flex;gap:19px;font-size:12.5px;color:var(--text-dark)}
.account-nav{left:856px;top:27px;font-size:12.5px;color:var(--text-dark)}
.patient-link{left:962px;top:26px;font-size:12.5px;color:var(--brand);display:flex;align-items:center;gap:7px}
.social{display:flex;gap:10px}
.social span{border-radius:50%;display:block}
.header-social{left:1089px;top:26px}
.header-social span{width:15px;height:15px;background:var(--brand-dark)}
.page-title{left:0;top:128px;width:1200px;text-align:center;font-size:44px;color:var(--brand);font-weight:400}
.profile-card{left:161px;top:213px;width:878px;height:395px;background:var(--white);box-shadow:0 1px 4px rgba(0,0,0,.18)}
.profile-side{position:absolute;left:0;top:0;width:277px;height:395px;background:var(--panel-bg)}
.photo{position:absolute;left:50px;top:29px;width:178px;height:178px;border-radius:50%;background:radial-gradient(circle at 50% 45%,#c9a07f 0 30%,#4a6b3a 55%,#2e4a25 100%)}
.doc-name{position:absolute;left:0;top:221px;width:277px;text-align:center;color:var(--brand);font-weight:700;font-size:14px}
.doc-role{position:absolute;left:0;top:241px;width:277px;text-align:center;color:#333;font-size:12.5px}
.stats{position:absolute;left:37px;top:264px;width:205px;height:42px;background:var(--white);border-radius:8px;display:flex}
.stat{flex:1;text-align:center;padding-top:7px}
.stat+.stat{border-left:1px solid #ddd}
.stat b{display:block;font-size:12px;color:#8a8a8a}
.stat small{display:block;font-size:10px;color:#999;margin-top:2px}
.book-btn{position:absolute;left:78px;top:327px;width:120px;height:36px;background:var(--brand);color:var(--white);border-radius:2px;font-size:13px;text-align:center;line-height:36px;letter-spacing:-.3px}
.profile-info{position:absolute;left:306px;top:0;width:550px}
.profile-info h2{position:absolute;left:0;font-size:17.5px;font-weight:700;color:var(--text)}
.profile-info p{position:absolute;left:0;width:540px;font-size:17.5px;line-height:21px;color:var(--text)}
.site-footer{left:0;top:676px;width:1200px;height:234px;background:var(--footer-bg)}
.footer-brand{left:78px;top:722px;font-size:42px}
.footer-brand .brand-dot{width:32px;height:32px}
.footer-address{left:73px;top:795px;font-size:16px;line-height:26px;color:var(--text)}
.footer-col{top:723px}
.footer-col h3{font-size:16px;font-weight:700;color:var(--text);margin-bottom:9px}
.footer-col a{display:block;font-size:13px;color:var(--text-dark);text-decoration:none;line-height:29px}
.footer-social{left:918px;top:748px}
.footer-social span{width:24px;height:24px;background:#666}
.copyright-bar{left:0;top:910px;width:1200px;height:49px;background:var(--bar-bg);text-align:center;font-size:10.5px;line-height:49px;color:var(--text-dark)}
</style>
</head>
<body>
<header class="site-header">
  <div class="abs brand header-brand"><span class="brand-dot"></span>CalmHarbor</div>
  <nav class="abs main-nav"><span>For Practitioners</span><span>How it Works</span><span>Meet Our Team</span><span>Contact</span></nav>
  <div class="abs account-nav">Sign Up/Sign In</div>
  <div class="abs patient-link">
    <svg width="13" height="14" viewBox="0 0 13 14" fill="none" stroke="#888" stroke-width="1.1"><circle cx="6.5" cy="4" r="3"/><path d="M1 13.5c0-3 2.5-5 5.5-5s5.5 2 5.5 5"/></svg>
    Patient Sign In
  </div>
  <div class="abs social header-social"><span></span><span></span></div>
</header>

<h1 class="abs page-title">Dr. Liam Carden Detail</h1>

<section class="abs profile-card">
  <div class="profile-side">
    <div class="photo" role="img" aria-label="Portrait photo of Dr. Liam Carden outdoors among greenery"></div>
    <div class="doc-name">Dr. Liam Carden</div>
    <div class="doc-role">General Practitioner</div>
    <div class="stats">
      <div class="stat"><b>Experience</b><small>10 years</small></div>
      <div class="stat"><b>Available</b><small>Today, 1:45 pm</small></div>
    </div>
    <div class="book-btn">Book Now</div>
  </div>
  <div class="profile-info">
    <h2 style="top:24px">About</h2>
    <p style="top:70px">Liam is a GP that has specialist mental health training and regularly sees patients that are looking for assistance with anxiety or depression.</p>
    <p style="top:154px">He is also interested in holistic healthcare, and regularly practices yoga as well as meditation.</p>
    <h2 style="top:213px">Languages</h2>
    <p style="top:259px">English</p>
    <h2 style="top:297px">Specialities</h2>
    <p style="top:343px">Anxiety, Depression, Sleeping issues</p>
  </div>
</section>

<footer class="abs site-footer"></footer>
<div class="abs brand footer-brand"><span class="brand-dot"></span>CalmHarbor</div>
<address class="abs footer-address" style="font-style:normal">Harbour Point,<br>Coastal District 2100,<br>Australia</address>
<div class="abs footer-col" style="left:473px">
  <h3>EXPLORE</h3>
  <a>For Practitioners</a><a>How it Works</a><a>Meet Our Team</a><a>Contact</a>
</div>
<div class="abs footer-col" style="left:676px">
  <h3>ABOUT US</h3>
  <a>Who We Are</a><a>Help &amp; FAQs</a><a>Privacy Policy</a><a>Terms &amp; Conditions</a>
</div>
<div class="abs footer-col" style="left:918px"><h3>GET CONNECTED</h3></div>
<div class="abs social footer-social"><span></span><span></span></div>
<div class="abs copyright-bar">Copyright © 2020&nbsp; CalmHarbor. All Rights Reserved.</div>
</body>
</html>
```